Logo & Business Card Design for Law Firm
Harlow Law Group
Logo & Business Card Design for Law Firm - Law
Creative Brief
Trial Lawyers
I am looking for a bold logo and business card design for a start-up law firm based in Philadelphia and with offices in PA and NJ. Harlow Law Group is led by trial attorneys and specializes in catastrophic personal injury litigation stemming from construction / industrial accidents, truck/auto accidents, defective products, falls, and medical malpractice.
I am looking for a design that displays an image that is modern, clean, and somewhat minimalist while at the same time conveys that the Harlow Law Group brand is serious. I am not looking for some hokey integration of the scales of justice or anything along those played-out lines. The color palate for the design is flexible; however, I am partial to blues, greens, and reds.
For the business card, I am looking for something that is dual-sided. The front should display the logo, attorney name (with Trial Lawyer as the title beneath the name - use Derek T. Harlow, as the name for the sample), address (2700 Bramble Avenue, 32nd Floor, Philadelphia, PA 19104), phone, fax, and website (www.harlowtrialfirm.example). If there is room, I may also add my NJ office location - assuming it doesn't overload the image. The back of the card should list my areas of expertise: Serious Injuries / Wrongful Death, Brain Injuries, Construction Accidents, Industrial Accidents, Truck Accidents, Car Accidents, Defective Products, Electrocution Injuries, Burn Injuries, Slip/Trip and Falls, and Commercial Litigation.
Professional
Color selection is flexible; however, I tend to prefer blues, greens, and reds.

```html
<!DOCTYPE html>
<html lang="en">
<head>
<meta charset="utf-8">
<title>Harlow Law Group – Business Card</title>
<link rel="stylesheet" href="https://fonts.googleapis.com/css2?family=Cinzel:wght@400;500&family=Roboto+Condensed:wght@400&display=swap">
<style>
  :root {
    --page-bg: #eef0f2;
    --card-bg: #ffffff;
    --card-shade: #f1f3f5;
    --brand-blue: #2f72b8;
    --text-dark: #2b2b2b;
    --text-muted: #8a8d91;
    --rule: #b9bcc0;
  }
  * { box-sizing: border-box; margin: 0; padding: 0; }
  html, body {
    width: 1200px;
    height: 1000px;
    overflow: hidden;
    background: var(--page-bg);
  }
  .business-card {
    position: absolute;
    left: 100px;
    top: 214px;
    width: 1000px;
    height: 572px;
    background: linear-gradient(135deg, var(--card-bg) 0%, var(--card-bg) 55%, var(--card-shade) 100%);
    box-shadow: 0 6px 24px rgba(0, 0, 0, 0.12);
  }
  .brand {
    position: absolute;
    left: 70px;
    top: 150px;
    display: flex;
    align-items: center;
    gap: 22px;
  }
  .brand-dot {
    width: 64px;
    height: 64px;
    border-radius: 50%;
    background: var(--brand-blue);
  }
  .brand-name {
    font-family: "Cinzel", serif;
    font-weight: 500;
    font-size: 40px;
    letter-spacing: 2px;
    color: var(--brand-blue);
    text-transform: uppercase;
  }
  .attorney {
    position: absolute;
    left: 70px;
    top: 328px;
    width: 440px;
  }
  .attorney-name {
    font-family: "Cinzel", serif;
    font-weight: 500;
    font-size: 42px;
    letter-spacing: 1px;
    color: var(--brand-blue);
    text-transform: uppercase;
    line-height: 1;
  }
  .attorney-title {
    display: flex;
    align-items: center;
    gap: 10px;
    margin-top: 8px;
    font-family: "Roboto Condensed", sans-serif;
    font-size: 22px;
    letter-spacing: 1px;
    color: var(--text-muted);
    text-transform: uppercase;
  }
  .attorney-title::before {
    content: "";
    flex: 1;
    height: 2px;
    background: linear-gradient(90deg, transparent, var(--rule));
  }
  .office {
    position: absolute;
    left: 640px;
    font-family: "Roboto Condensed", sans-serif;
    font-size: 21px;
    line-height: 1.35;
    color: var(--text-dark);
  }
  .office-main { top: 60px; }
  .office-nj { top: 330px; }
  .office .street { text-transform: uppercase; }
</style>
</head>
<body>
  <main class="business-card">
    <div class="brand">
      <span class="brand-dot"></span>
      <span class="brand-name">Harlow Law Group</span>
    </div>

    <div class="attorney">
      <p class="attorney-name">Derek T. Harlow</p>
      <p class="attorney-title">Founder</p>
    </div>

    <address class="office office-main">
      <span class="street">2700 Bramble Avenue,<br>32nd Floor, Philadelphia,<br>PA 19104</span><br>
      Call: (1)215 555 0148<br>
      Mail info@harlowtrialfirm.example<br>
      www.harlowtrialfirm.example
    </address>

    <address class="office office-nj">
      NJ office location<br>
      <span class="street">32nd Floor, Philadelphia, PA 19104</span><br>
      Call: (1)215 555 0148<br>
      Mail info@harlowtrialfirm.example<br>
      www.harlowtrialfirm.example
    </address>
  </main>
</body>
</html>
```